Helen's 40th Invitation

I need an invitation designed for a 40th birthday in Singapore. The theme is a "long lunch", set in a colonial garden (black and white house - Singapore style if you want to Google or Bing it).
Look and feel should be simple, elegant, stylish, bold, fresh, minimalist. Nothing fussy, intricate, formal or too colourful. No intials, not wedding-like, minimal colour (no golds).
Setting will be garden setting with champagne, white marquee, white table cloths, long trestle tables, fresh white floowers (lilys or hydrangas).
Format should be PC friendly (jpeg, gif, pdf etc).
Size is flexible to accomodate design - it will be emailed as an attachment.
Details to include:
- Saturday, 27th November, 2010
Time - From 1pm.
Address - 215 Thornbury Park, Singapore
Dress: Garden Glam
RSVP - jlowden@tevarondi.com by 13 November, 2010

```html
<!DOCTYPE html>
<html lang="en">
<head>
<meta charset="utf-8">
<title>Long Lunch – Helen's 40th</title>
<link rel="stylesheet" href="https://fonts.googleapis.com/css2?family=Bodoni+Moda:opsz,wght@6..96,400&family=Varela+Round&family=Roboto+Condensed:wght@400;700&display=swap">
<style>
  :root {
    --page: #ffffff;
    --bark: #3c2214;
    --leaf-deep: #1f6b3e;
    --leaf-soft: #5fa777;
    --ink-light: #ffffff;
  }
  * { margin: 0; padding: 0; box-sizing: border-box; }
  html, body {
    width: 1200px;
    height: 900px;
    overflow: hidden;
    background: var(--page);
  }
  .canvas {
    position: relative;
    width: 1200px;
    height: 900px;
    background: var(--page);
  }
  .invitation {
    position: absolute;
    left: 100px;
    top: 186px;
    width: 994px;
    height: 504px;
    background: var(--bark);
    overflow: hidden;
  }
  .vine-artwork {
    position: absolute;
    left: 0;
    top: 0;
    width: 960px;
    height: 360px;
    background:
      radial-gradient(ellipse 60% 35% at 45% 40%, rgba(95, 167, 119, 0.45), rgba(31, 107, 62, 0.25) 55%, rgba(60, 34, 20, 0) 80%);
  }
  .title {
    position: absolute;
    left: 0;
    top: 0;
    width: 994px;
    height: 180px;
  }
  .title text {
    font-family: "Bodoni Moda", "Didot", serif;
    font-weight: 400;
    fill: var(--ink-light);
  }
  .occasion {
    position: absolute;
    right: 26px;
    top: 178px;
    font-family: "Varela Round", "Nunito", sans-serif;
    font-size: 40px;
    line-height: 1;
    color: var(--ink-light);
  }
  .details {
    position: absolute;
    left: 0;
    top: 326px;
    width: 994px;
    text-align: center;
    font-family: "Roboto Condensed", "Arial Narrow", sans-serif;
    font-size: 23px;
    color: var(--ink-light);
    list-style: none;
  }
  .details li {
    height: 42px;
    line-height: 42px;
  }
  .details strong { font-weight: 700; }
</style>
</head>
<body>
<main class="canvas">
  <section class="invitation">
    <div class="vine-artwork" role="img" aria-label="Green climbing vine with curling tendrils and leaves sweeping across the top of the card"></div>

    <svg class="title" viewBox="0 0 994 180" aria-label="Long Lunch">
      <text x="24" y="138" font-size="152" textLength="942" lengthAdjust="spacingAndGlyphs">LONG LUNCH</text>
    </svg>

    <p class="occasion">Helen's 40th</p>

    <ul class="details">
      <li>Saturday, <strong>27th Nov 2010</strong> From <strong>1pm</strong></li>
      <li><strong>VENUE</strong> 215 Thornbury Park, Singapore</li>
      <li>Dress <strong>Garden Glam</strong></li>
      <li><strong>RSVP</strong> jlowden@tevarondi.com by <strong>13th Nov 2010</strong></li>
    </ul>
  </section>
</main>
</body>
</html>
```